Fitness competition business needs a card design

I need a professional business card design using my logo. The card will be horizontal with rounded edges.

Target Market(s)

Female fitness competitors

Industry/Entity Type

Fitness

Contact Information for Business Card

Rose-Lynn Darby
Owner
stagevarno.com
555.301.2187
info@stagevarno.com

Font styles to use
Serif

Colors

Designer to choose colors to be used in the design.

Requirements
Must have
• On the back please add the following:
• Figure
• Bikini
• Physique
• Fitness
Nice to have
• Looking for a very sleek design, contemporary and easy to read.
Should not have
• Should not be difficult to read or be too busy

```html
<!DOCTYPE html>
<html lang="en">
<head>
<meta charset="utf-8">
<title>Stage Varno – Business Card</title>
<link rel="stylesheet" href="https://fonts.googleapis.com/css2?family=Playfair+Display:wght@700&family=Lora:wght@400;700&display=swap">
<style>
  :root {
    --backdrop: #acacac;
    --card-white: #ffffff;
    --brand-red: #ec2129;
    --brand-grey: #5b5c5e;
    --ink: #1d1d1b;
    --rule: #8a8aa0;
  }
  * { box-sizing: border-box; margin: 0; padding: 0; }
  html, body {
    width: 1200px; height: 900px; overflow: hidden;
    background: var(--backdrop);
  }
  .card {
    position: absolute; top: 310px;
    width: 490px; height: 280px;
    border-radius: 14px; overflow: hidden;
  }
  .card--front { left: 90px; background: var(--card-white); }
  .card--back { left: 620px; background: var(--brand-grey); }

  .wordmark {
    font-family: "Playfair Display", Georgia, serif;
    font-weight: 700; letter-spacing: 1.5px;
    text-align: center;
  }

  /* front */
  .front__brand {
    position: absolute; left: 0; top: 0; width: 230px; height: 100%;
    display: flex; align-items: center; justify-content: center;
  }
  .card--front .wordmark {
    font-size: 32px; line-height: 38px; color: var(--brand-red);
  }
  .front__divider {
    position: absolute; left: 230px; top: 50px;
    width: 1px; height: 180px; background: var(--rule);
  }
  .contact {
    position: absolute; left: 231px; top: 0; width: 259px; height: 100%;
    display: flex; flex-direction: column; justify-content: center;
    text-align: center;
    font-family: "Lora", Georgia, serif;
    font-size: 13px; color: var(--ink);
  }
  .contact__name {
    font-family: "Playfair Display", Georgia, serif;
    font-weight: 700; font-size: 19px; line-height: 24px;
    letter-spacing: 0.3px; color: var(--brand-grey);
  }
  .contact__name .first { color: var(--brand-red); }
  .contact__title {
    font-size: 12px; letter-spacing: 2px; text-transform: uppercase;
    color: var(--brand-grey); margin: 2px 0 10px;
  }
  .contact__rule {
    width: 156px; height: 1px; background: var(--rule); margin: 0 auto;
  }
  .contact__lines { padding: 8px 0 7px; line-height: 20px; }
  .label { color: var(--brand-red); }
  .contact__web { color: var(--brand-red); font-weight: 700; }
  .contact__address { padding-top: 6px; line-height: 17px; }

  /* back */
  .back__band {
    position: absolute; left: 0; top: 0; width: 100%; height: 130px;
    background: var(--brand-red);
  }
  .card--back .wordmark {
    position: absolute; left: 0; top: 106px; width: 100%;
    font-size: 36px; line-height: 48px; color: var(--card-white);
  }
  .divisions {
    position: absolute; left: 0; top: 186px; width: 100%;
    text-align: center;
    font-family: "Lora", Georgia, serif;
    font-size: 13px; letter-spacing: 2.5px; color: var(--card-white);
  }
  .divisions .dot { color: var(--brand-red); padding: 0 6px; }
  .back__web {
    position: absolute; left: 0; top: 236px; width: 100%;
    text-align: center;
    font-family: "Lora", Georgia, serif;
    font-weight: 700; font-size: 13px; color: var(--card-white);
  }
</style>
</head>
<body>
  <section class="card card--front">
    <div class="front__brand"><div class="wordmark">STAGE<br>VARNO</div></div>
    <div class="front__divider"></div>
    <div class="contact">
      <p class="contact__name"><span class="first">ROSE-LYNN</span> DARBY</p>
      <p class="contact__title">Owner</p>
      <div class="contact__rule"></div>
      <div class="contact__lines">
        <p><span class="label">P:</span> 555.301.2187</p>
        <p><span class="label">E:</span> info@stagevarno.com</p>
        <p class="contact__web">www.stagevarno.com</p>
      </div>
      <div class="contact__rule"></div>
      <div class="contact__address">
        <p>1234, Address Goes Here</p>
        <p>Country Name, 123456</p>
      </div>
    </div>
  </section>

  <section class="card card--back">
    <div class="back__band"></div>
    <div class="wordmark">STAGE VARNO</div>
    <p class="divisions">FIGURE<span class="dot">•</span>BIKINI<span class="dot">•</span>PHYSIQUE<span class="dot">•</span>FITNESS</p>
    <p class="back__web">www.stagevarno.com</p>
  </section>
</body>
</html>
```